I am a company selling interior designing materials

HI, I am selling interior design materials and require a namecard which is more outstanding while following a certain details placement as attached.

My clients are mainly interior designers so it has to attract their attention rather than feeling that its "just another namecard". I am selling wallcoverings, fabrics, acoustics and carpets.

Target Market(s)

interior designers designing hotels, commerical offices.

Contact Information for Business Card

As per attached.
Please change address to 47 Jalan 16 Tampines #05-02 Velmora Building Singapore 527314

Font styles to use
Other font styles liked:
• calibri

Requirements
Must have
• (1) company logo on top in the middle. Placement of contac details to be the same
• (2) company color is blue/green cymk 75/8/42/0
• (3) "KTV" logo to be prominent
• (4) You may change the logo but there should be a "swirl" surrounding the word KTV like current logo. The swirl pattern does not need to follow current logo and you may propose.
Should not have
• (1) there should not be any designs above "KTV" logo
• (2) no sharp triangles or angles

```html
<!DOCTYPE html>
<html lang="en">
<head>
<meta charset="utf-8">
<title>KTV Business Card – Front and Back</title>
<link rel="stylesheet" href="https://fonts.googleapis.com/css2?family=Noto+Serif:wght@700&family=PT+Sans:wght@700&display=swap">
<style>
  :root {
    --pasteboard: #5b5b5b;
    --paper: #ffffff;
    --brand-teal: #1ba89f;
    --accent-red: #e30f23;
    --slate: #6d6b69;
    --logo-grey: #636363;
    --mark-line: #333333;
    --serif: "Noto Serif", Georgia, serif;
    --sans: "PT Sans", Calibri, Arial, sans-serif;
  }
  html, body { margin: 0; padding: 0; overflow: hidden; }
  body { width: 846px; height: 1200px; background: var(--pasteboard); }
  .canvas { position: relative; width: 846px; height: 1200px; overflow: hidden; }
  .artwork { position: absolute; inset: 0; }
  .text { position: absolute; margin: 0; white-space: nowrap; line-height: 1; }

  .wordmark { font-family: var(--serif); font-weight: 700; color: var(--logo-grey); left: 0; width: 846px; text-align: center; }
  .wordmark--front { top: 140px; font-size: 40px; letter-spacing: 1px; }
  .wordmark--back { top: 772px; font-size: 80px; letter-spacing: 2px; }

  .company-name { font-family: var(--serif); font-weight: 700; color: var(--brand-teal); font-size: 13.5px; top: 214px; left: 0; width: 846px; text-align: center; }
  .person-name { font-family: var(--serif); font-weight: 700; color: var(--accent-red); font-size: 51px; top: 259px; left: 0; width: 846px; text-align: center; }
  .mobile { font-family: var(--sans); font-weight: 700; color: var(--slate); font-size: 27px; top: 317px; left: 0; width: 846px; text-align: center; }

  .contact { font-family: var(--sans); font-weight: 700; color: var(--paper); font-size: 17.5px; line-height: 24px; top: 424px; }
  .contact--address { left: 122px; }
  .contact--lines { right: 125px; text-align: right; }

  .services { font-family: var(--serif); font-weight: 700; color: var(--paper); font-size: 28px; top: 1030px; left: 0; width: 846px; text-align: center; word-spacing: 4px; }
  .services span + span { margin-left: 22px; }
</style>
</head>
<body>
<main class="canvas">
  <svg class="artwork" viewBox="0 0 602 854" width="846" height="1200" preserveAspectRatio="none" aria-hidden="true">
    <defs>
      <g id="card-swoosh">
        <path fill="var(--brand-teal)" d="M40,235 C120,275 250,290 390,262 C470,245 530,215 558,205 L558,365 L40,365 Z"/>
        <path fill="var(--accent-red)" d="M40,198 C130,250 280,275 390,262 C250,290 120,275 40,235 Z"/>
        <path fill="var(--slate)" d="M300,272 C420,258 510,212 558,170 L558,205 C530,215 470,245 390,262 C360,268 330,271 300,272 Z"/>
      </g>
      <g id="crop-marks" stroke="var(--mark-line)" stroke-width="0.6" fill="none">
        <line x1="40" y1="12" x2="40" y2="42"/>
        <line x1="70" y1="12" x2="70" y2="52"/>
        <line x1="10" y1="50" x2="40" y2="50"/>
        <line x1="528" y1="12" x2="528" y2="52"/>
        <line x1="558" y1="12" x2="558" y2="42"/>
        <line x1="558" y1="50" x2="590" y2="50"/>
        <line x1="300" y1="14" x2="300" y2="62"/>
        <line x1="265" y1="38" x2="335" y2="38"/>
        <line x1="40" y1="145" x2="40" y2="300"/>
        <line x1="10" y1="210" x2="56" y2="210"/>
        <line x1="544" y1="210" x2="590" y2="210"/>
        <line x1="40" y1="345" x2="40" y2="408"/>
        <line x1="70" y1="345" x2="70" y2="408"/>
        <line x1="10" y1="345" x2="70" y2="345"/>
        <line x1="528" y1="345" x2="528" y2="408"/>
        <line x1="558" y1="345" x2="558" y2="408"/>
        <line x1="528" y1="345" x2="590" y2="345"/>
        <line x1="300" y1="358" x2="300" y2="408"/>
        <line x1="265" y1="380" x2="335" y2="380"/>
      </g>
    </defs>

    <rect class="sheet" x="10" y="12" width="580" height="398" fill="var(--paper)"/>
    <rect class="sheet" x="10" y="440" width="580" height="400" fill="var(--paper)"/>

    <use href="#card-swoosh"/>
    <use href="#card-swoosh" transform="translate(0,432)"/>

    <use href="#crop-marks"/>
    <use href="#crop-marks" transform="translate(0,430)"/>
  </svg>

  <section class="card card--front">
    <p class="text wordmark wordmark--front">KTV</p>
    <p class="text company-name">KelTavio Interior Furnishings Pte Ltd</p>
    <h1 class="text person-name">Rachel Ong</h1>
    <p class="text mobile">(65) 9172 4630</p>
    <p class="text contact contact--address">47 Jalan 16 Tampines #05-02<br>Velmora Building Singapore 527314</p>
    <p class="text contact contact--lines">(65) 6283 5174<br>rachel@ktvfurnishings.com</p>
  </section>

  <section class="card card--back">
    <p class="text wordmark wordmark--back">KTV</p>
    <p class="text services"><span>Wallcoverings</span><span>Acoustic</span><span>Fabrics</span><span>Carpet</span></p>
  </section>
</main>
</body>
</html>
```